Crimson Vantage Cleaning Solutions

Need a logo and business card design. I want to use a translucent business card. I want to abbreviate the name C.V.C.S. Commercial Cleaning, because my is Dov. I’d also like to incorporate a knight or something like that. I want the idea to tie in with the word Crimson. New ideas are welcome, i don’t want to limit anyone’s creativity.

Target Market(s)

Commercial Cleaning for businesses.

Contact Information for Business Card

Crimson
Vantage
Cleaning
Solutions

```html
<!DOCTYPE html>
<html lang="en">
<head>
<meta charset="utf-8">
<title>Crimson Vantage Cleaning Solutions – Business Card</title>
<link rel="stylesheet" href="https://fonts.googleapis.com/css2?family=Roboto:wght@400;500;700&display=swap">
<style>
  :root {
    --page: #ece8e2;
    --card: #ffffff;
    --navy: #1f3f9c;
    --brand-blue: #2a58b8;
    --accent-orange: #f07a1a;
    --ink: #1a1a1a;
    --icon-blue: #2a8fd6;
    --rule: #222222;
    --faint-mark: #dfe7f3;
  }
  * { margin: 0; padding: 0; box-sizing: border-box; }
  html, body { width: 900px; height: 1200px; overflow: hidden; }
  body {
    background: var(--page);
    font-family: "Roboto", Arial, sans-serif;
    position: relative;
    color: var(--ink);
  }
  .card {
    position: absolute;
    left: 82px;
    width: 733px;
    height: 428px;
    background: var(--card);
    border-radius: 24px;
    box-shadow: 0 3px 10px rgba(0,0,0,0.18);
    overflow: hidden;
  }
  .card--front { top: 138px; }
  .card--back { top: 634px; }

  .brand-mark {
    position: absolute;
    border-radius: 50%;
    background: var(--brand-blue);
  }
  .card--front .brand-mark { left: 58px; top: 50px; width: 100px; height: 100px; }
  .card--back .brand-mark { left: 100px; top: 150px; width: 104px; height: 104px; }

  .faint-mark {
    position: absolute;
    right: -20px;
    top: 20px;
    width: 210px;
    height: 210px;
    border-radius: 50%;
    background: var(--faint-mark);
    opacity: 0.7;
  }

  .brand-name {
    position: absolute;
    font-weight: 700;
    color: var(--navy);
    line-height: 1.05;
    letter-spacing: -0.5px;
  }
  .card--front .brand-name { left: 188px; top: 62px; font-size: 38px; }
  .card--back .brand-name { left: 246px; top: 156px; font-size: 40px; }

  .brand-tagline {
    position: absolute;
    color: var(--accent-orange);
    font-size: 15px;
  }
  .card--front .brand-tagline { left: 189px; top: 144px; }
  .card--back .brand-tagline { left: 248px; top: 242px; font-size: 16px; }

  .holder-name {
    position: absolute;
    left: 51px; top: 228px;
    font-size: 22px;
  }
  .holder-title {
    position: absolute;
    left: 52px; top: 257px;
    font-size: 16px;
    color: var(--navy);
  }
  .title-rule {
    position: absolute;
    left: 173px; top: 272px;
    width: 508px; height: 1px;
    background: var(--rule);
  }
  .contact-list {
    position: absolute;
    left: 51px; top: 288px;
    list-style: none;
    font-size: 16px;
  }
  .contact-list li {
    display: flex;
    align-items: center;
    height: 25.5px;
  }
  .contact-list svg { width: 15px; height: 15px; margin-right: 10px; fill: var(--icon-blue); }
  .address {
    position: absolute;
    right: 52px; top: 288px;
    text-align: right;
    font-size: 16px;
    line-height: 25.5px;
    font-style: normal;
  }
</style>
</head>
<body>
  <section class="card card--front" aria-label="Card front">
    <div class="faint-mark" aria-hidden="true"></div>
    <div class="brand-mark" aria-hidden="true"></div>
    <div class="brand-name">Crimson Vantage<br>Cleaning Solutions</div>
    <div class="brand-tagline">C.V.C.S. Commercial Cleaning</div>

    <div class="holder-name">Marcus Whitfield</div>
    <div class="holder-title">CEO/Founder</div>
    <div class="title-rule"></div>

    <ul class="contact-list">
      <li><svg viewBox="0 0 24 24"><path d="M6.6 10.8a15.1 15.1 0 0 0 6.6 6.6l2.2-2.2c.3-.3.7-.4 1-.2 1.1.4 2.3.6 3.6.6.6 0 1 .4 1 1V20c0 .6-.4 1-1 1C10.6 21 3 13.4 3 4c0-.6.4-1 1-1h3.5c.6 0 1 .4 1 1 0 1.3.2 2.5.6 3.6.1.3 0 .7-.2 1z"/></svg>214-555-0186</li>
      <li><svg viewBox="0 0 24 24"><path d="M6 2h12v5H6zM3 8h18a1 1 0 0 1 1 1v8h-4v5H6v-5H2V9a1 1 0 0 1 1-1zm5 8v4h8v-4z"/></svg>214-555-0186</li>
      <li><svg viewBox="0 0 24 24"><path d="M2 5h20v14H2zm2 2v.5l8 5 8-5V7l-8 5z"/></svg>dov@crimsonvantage.com</li>
      <li><svg viewBox="0 0 24 24"><path d="M12 2a10 10 0 1 0 0 20 10 10 0 0 0 0-20zm6.9 6h-3a15 15 0 0 0-1.3-4 8 8 0 0 1 4.3 4zM12 4c.8 1.2 1.4 2.5 1.8 4h-3.6c.4-1.5 1-2.8 1.8-4zM4.3 14a8 8 0 0 1 0-4h3.4a16 16 0 0 0 0 4zm.8 2h3a15 15 0 0 0 1.3 4 8 8 0 0 1-4.3-4zm3-8h-3a8 8 0 0 1 4.3-4A15 15 0 0 0 8.1 8zM12 20c-.8-1.2-1.4-2.5-1.8-4h3.6c-.4 1.5-1 2.8-1.8 4zm2.3-6H9.7a14 14 0 0 1 0-4h4.6a14 14 0 0 1 0 4zm.3 6a15 15 0 0 0 1.3-4h3a8 8 0 0 1-4.3 4zm1.7-6a16 16 0 0 0 0-4h3.4a8 8 0 0 1 0 4z"/></svg>www.crimsonvantageclean.com</li>
    </ul>

    <address class="address">418 Harbor Street NW<br>Suite 210, Lakeview<br>MI 49872</address>
  </section>

  <section class="card card--back" aria-label="Card back">
    <div class="brand-mark" aria-hidden="true"></div>
    <div class="brand-name">Crimson Vantage<br>Cleaning Solutions</div>
    <div class="brand-tagline">C.V.C.S. Commercial Cleaning</div>
  </section>
</body>
</html>
```